" A nossa empresa trabalha com um vale-refeição digital. Fechamos contratos com restaurantes para que eles possam receber a nossa forma de pagamento (cartãozinho do Grupo da Mesada e QR CODE do celular do usuário). Fechamos, então, contratos com empresas para que elas usem o nosso vale-refeição digital, com os usuários delas podendo pesquisar por prato (cardápio), estilo de comida (a la carte, buffet), estilo de cozinha (italiana, alemã, etc) na região onde trabalham (geolocalização) "

```html
<!DOCTYPE html>
<html lang="pt-BR">
<head>
<meta charset="utf-8">
<title>Grupo da Mesada — Página 02</title>
<link rel="stylesheet" href="https://fonts.googleapis.com/css2?family=Montserrat:wght@400;600;700&display=swap">
<style>
  :root {
    --stage: #e9e4df;
    --page: #f6f5f4;
    --ink: #3a3434;
    --muted: #8d8787;
    --brand: #d8323a;
    --brand-soft: #f7dfe0;
    --line: #e4dede;
    --card: #ffffff;
  }
  * { box-sizing: border-box; margin: 0; padding: 0; }
  html, body { width: 1200px; height: 1200px; overflow: hidden; }
  body {
    background: var(--stage);
    font-family: "Montserrat", sans-serif;
    color: var(--ink);
    position: relative;
  }
  .page {
    position: absolute;
    left: 50px; top: 187px;
    width: 1100px; height: 825px;
    background: linear-gradient(180deg, #ffffff 0%, var(--page) 100%);
    overflow: hidden;
  }
  .photo { position: absolute; }
  .photo--salad {
    left: 7px; top: 65px; width: 205px; height: 395px;
    background: linear-gradient(160deg, #f1c56c 0%, #d9473a 35%, #7aa24b 65%, #e9e3d6 100%);
  }
  .photo--plate {
    left: 662px; top: 54px; width: 432px; height: 432px; border-radius: 50%;
    background: radial-gradient(circle at 50% 50%, #8a9a4a 0%, #c9773b 30%, #3b3a36 55%, #1f1e1c 75%);
  }
  .photo--pasta {
    left: 22px; top: 590px; width: 150px; height: 115px; border-radius: 50%;
    background: radial-gradient(circle, #c2552b 0%, #e39a4d 55%, #f1ece4 80%);
  }
  .photo--pancakes {
    left: 205px; top: 504px; width: 216px; height: 270px;
    background: linear-gradient(180deg, #c0203f 0%, #e6b06a 40%, #d99450 75%, #f3eee8 100%);
  }
  .card {
    position: absolute;
    background: var(--card);
    box-shadow: 0 2px 8px rgba(0,0,0,.12);
  }
  .card--pasta { left: 7px; top: 540px; width: 180px; height: 180px; }
  .rating {
    position: absolute;
    display: flex; align-items: center; justify-content: space-between;
    height: 26px; padding: 0 8px;
    font-size: 13px; color: var(--brand); letter-spacing: 2px;
    background: var(--card);
    box-shadow: 0 1px 4px rgba(0,0,0,.1);
  }
  .rating .icons { display: flex; gap: 8px; align-items: center; color: var(--muted); }
  .rating .icons .heart { color: var(--brand); }
  .rating--salad { left: 7px; top: 466px; width: 205px; }
  .rating--pasta { left: 7px; top: 548px; width: 180px; box-shadow: none; }
  .rating--middle { left: 240px; top: 462px; width: 195px; }
  .rating--offer { left: 760px; top: 570px; width: 113px; }
  .brand {
    position: absolute; left: 280px; top: 62px; width: 320px;
    display: flex; flex-direction: column; align-items: center; gap: 12px;
  }
  .brand__dot { width: 64px; height: 64px; border-radius: 50%; background: var(--brand); }
  .brand__name { font-size: 34px; font-weight: 700; color: var(--brand); letter-spacing: -0.5px; }
  .about {
    position: absolute; left: 288px; top: 255px; width: 367px;
    font-size: 14.5px; line-height: 24px; text-align: justify; color: var(--ink);
  }
  .about strong, .about b { font-weight: 700; }
  .offer {
    position: absolute; left: 488px; top: 605px; width: 385px; height: 115px;
    background: var(--card);
    border: 2px solid var(--brand);
    padding: 14px 16px;
  }
  .offer__title { font-size: 14px; font-weight: 600; color: var(--brand); line-height: 19px; width: 250px; }
  .offer__note { font-size: 9.5px; color: var(--muted); margin-top: 10px; width: 250px; line-height: 13px; }
  .offer__price {
    position: absolute; right: 14px; bottom: 38px;
    font-size: 18px; font-weight: 700; color: var(--ink);
  }
  .offer__heart { position: absolute; right: 22px; bottom: 12px; color: var(--brand); font-size: 16px; }
  .social {
    position: absolute; left: 806px; top: 775px;
    display: flex; gap: 24px;
  }
  .social span { width: 22px; height: 22px; border-radius: 50%; background: var(--brand); display: block; }
  .band { position: absolute; left: 0; bottom: 0; width: 100%; height: 10px; background: var(--brand); }
  .topline { position: absolute; left: 0; top: 0; width: 100%; height: 6px; background: var(--brand-soft); }
</style>
</head>
<body>
  <main class="page">
    <div class="topline"></div>

    <div class="photo photo--salad" role="img" aria-label="Foto de salada colorida com tomates, pimentões e folhas"></div>
    <div class="rating rating--salad"><span>★★★☆☆</span><span class="icons"><span class="heart">♥</span><span>⤴</span></span></div>

    <div class="brand">
      <span class="brand__dot"></span>
      <span class="brand__name">Grupo da Mesada</span>
    </div>

    <p class="about"><b>O Grupo da Mesada</b> é uma empresa que desenvolve uma plataforma inteligente de descontos, recomendações e busca de restaurantes, com benefícios exclusivos. Com ele, você tem fácil acesso a milhares de estabelecimentos, pratos e cardápios, conseguindo os melhores preços direto no seu <b>celular</b>.</p>

    <div class="rating rating--middle"><span>★★★★☆</span><span class="icons"><span class="heart">♥</span><span>⤴</span></span></div>

    <div class="photo photo--plate" role="img" aria-label="Foto de prato escuro com camarões e macarrão de arroz com legumes"></div>

    <div class="card card--pasta"></div>
    <div class="rating rating--pasta"><span>★★★★☆</span><span class="icons"><span class="heart">♥</span><span>⤴</span></span></div>
    <div class="photo photo--pasta" role="img" aria-label="Foto de tigela de massa com molho de tomate"></div>

    <div class="photo photo--pancakes" role="img" aria-label="Foto de pilha de panquecas com frutas vermelhas"></div>

    <div class="rating rating--offer"><span>★★★★☆</span></div>
    <div class="offer">
      <p class="offer__title">Que tal receber novas ofertas para almoçar todos os dias no seu restaurante?</p>
      <p class="offer__note">Cadastre-se e receba descontos diários nos restaurantes perto do seu trabalho.</p>
      <span class="offer__price">12.90$</span>
      <span class="offer__heart">♥</span>
    </div>

    <div class="social"><span></span><span></span><span></span><span></span></div>
    <div class="band"></div>
  </main>
</body>
</html>
```